Need Help Rebranding My Food Blog

I have a Wordpress Food blog called BeetBuddies.com. Right now it has no life and is very bland. I am rebranding this site to a new named called, TheHoneyedDays.com. I would love to have a blog that is vibrant and full of life and personality.

One of my top priorities when a new visitor comes to my site is to quickly understand what the site is about (Gluten-free, dairy-free sweets that taste delicious).

I also want people to feel a connection with me when they come to the site.

Here are some other things that I'd like in the blog design...

1. Optin
My business is driven by adding people to my list so it is very important for me to have an optin front and center/ above-the-fold. See https://www.quietrevenuehub.com/ as an example. The headline that I would like is "Gluten-free & dairy-free sweets that actually taste good"

2. Vibrant/full life
The next important aspect of this blog is that it is vibrant. I like colors that remind me of a SUNSET. See attachments for logo and color scheme. Here's an example of a site I really like that is vibrant: http://www.mellowplateliving.com/

Also see Image titled: "Sample: Feeling". Notice the feeling you get from the image/brush strokes and how it feels light, breezy, and free spirited.

3. Food Images
The last important aspect for my blog is to showcase my recipes. I have attached a few of them as examples. Its really important for a food blog to showcase beautiful pictures of recipes for people to see so will definitely need this in the design.

Also, attached...
1. Image of me.
2. New logo for TheHoneyedDays (notice: don't use the one attached as "Sample/Feeling". That's just for reference of the feeling I like.)

Thanks!

Rosalind

P.S. I didn't include all the copy that would be needed so feel free to use the "lorem ipsum" text as placeholder if need be.

Target Market(s)

stay-at-home moms, dairy-free & gluten allergies, love desserts & sweets

Coding

Coded - Design and coding required

Font styles to use
Sans Serif

Requirements
Must have
• 1. Optin area with my picture and what I'm about ""Gluten-free & dairy-free sweets that actually taste good""
• 2. Must have personality/vibrancy to the site. Think full of life, not dull like my current website... beetbuddies.com
• 3. Highlight food images (Vertical image holders only)
Nice to have
• Color scheme should be based on my logo
Should not have
• No black or grey colors

```html
<!DOCTYPE html>
<html lang="en">
<head>
<meta charset="utf-8">
<title>TheHoneyedDays — Gluten-free &amp; dairy-free sweets</title>
<link rel="stylesheet" href="https://fonts.googleapis.com/css2?family=Open+Sans:wght@400;600;700&family=Montserrat:wght@600;700&display=swap">
<style>
:root{
  --pink:#e8456f;
  --coral:#f0614a;
  --orange:#f5833a;
  --green:#79b534;
  --green-soft:#cfe6b4;
  --peach:#fff4ee;
  --blush:#fde3e6;
  --mist:#f3f1f1;
  --ink:#4a3a3f;
  --muted:#9a8a8e;
  --line:#efe3e3;
  --white:#ffffff;
}
*{box-sizing:border-box;margin:0;padding:0}
html,body{width:1200px;height:2964px;overflow:hidden}
body{font-family:"Open Sans",sans-serif;color:var(--ink);background:var(--white);position:relative}
h1,h2,h3,h4{font-family:"Montserrat",sans-serif}
.wrap{position:absolute;left:160px;width:880px}

/* top bar */
.topbar{position:absolute;top:0;left:0;width:1200px;height:24px;background:linear-gradient(90deg,var(--pink),var(--orange));}
.topbar .links{position:absolute;left:160px;top:0;display:flex;height:24px}
.topbar .links a{color:var(--white);font-size:10px;font-weight:700;letter-spacing:.5px;text-decoration:none;padding:0 14px;line-height:24px}
.topbar .links a.active{background:rgba(255,255,255,.25)}
.topbar .social{position:absolute;right:160px;top:7px;display:flex;gap:8px}
.topbar .social span{width:10px;height:10px;border-radius:50%;background:var(--white);opacity:.9}

/* logo */
.brand{position:absolute;top:48px;left:0;width:1200px;text-align:center}
.brand .name{font-family:"Montserrat",sans-serif;font-weight:700;font-size:34px;color:var(--pink)}
.brand .dot{display:inline-block;width:14px;height:14px;border-radius:50%;background:var(--orange);margin-right:10px;vertical-align:middle}

/* category nav */
.catnav{top:140px;height:46px;border-top:1px solid var(--line);border-bottom:1px solid var(--line);display:flex;justify-content:center;gap:50px;align-items:center}
.catnav a{font-size:11px;font-weight:700;letter-spacing:1px;color:var(--ink);text-decoration:none}

/* hero */
.hero{top:220px;height:440px;background:radial-gradient(ellipse at 75% 30%,#e9c9a4,transparent 45%),linear-gradient(120deg,#5b3a2c,#8a5a40 40%,#c28a5e 70%,#6b4433);display:flex;align-items:center;justify-content:center}
.hero h1{font-family:"Open Sans",sans-serif;font-weight:400;color:var(--white);font-size:30px;line-height:1.3;text-align:center;max-width:520px;text-shadow:0 2px 6px rgba(60,30,20,.5)}

/* newsletter */
.newsletter{top:700px;height:220px;background:var(--mist);padding:42px 0 0 50px}
.newsletter h2{font-size:30px;font-weight:700;color:var(--ink)}
.newsletter p{font-size:12px;color:var(--muted);margin-top:12px;width:430px;line-height:1.6}
.newsletter form{display:flex;gap:12px;margin-top:18px}
.newsletter .field{width:300px;height:34px;border:1px solid #e2d8d8;background:var(--white);font-size:11px;color:var(--muted);padding:0 12px;line-height:34px}
.newsletter .btn{height:34px}
.newsletter .donuts{position:absolute;right:0;top:0;width:300px;height:220px;background:radial-gradient(circle at 30% 40%,#f6a5c0 0 18%,transparent 19%),radial-gradient(circle at 72% 62%,#f4c27a 0 20%,transparent 21%),radial-gradient(circle at 80% 20%,#8fd0e8 0 14%,transparent 15%),linear-gradient(135deg,#f7e7d6,#f2d1c0)}

/* buttons */
.btn{display:inline-flex;align-items:center;gap:8px;background:linear-gradient(90deg,var(--pink),var(--coral));color:var(--white);font-size:11px;font-weight:700;letter-spacing:.5px;padding:0 18px;height:32px;border:0}
.btn::after{content:"";border-left:6px solid var(--white);border-top:4px solid transparent;border-bottom:4px solid transparent}

/* posts */
.posts{position:absolute;top:950px;left:160px;width:560px;box-shadow:0 2px 12px rgba(200,150,150,.25);background:var(--white)}
.post{display:grid;grid-template-columns:280px 280px;height:400px}
.post .photo{position:relative;height:400px}
.post .text{padding:50px 26px 0}
.post h3{font-size:17px;line-height:1.3;font-weight:700;color:var(--ink)}
.post .meta{font-size:10px;color:var(--muted);margin-top:10px}
.post .cat{font-size:10px;font-weight:700;color:var(--pink);margin-top:6px;letter-spacing:.5px}
.post p{font-size:11px;line-height:1.7;color:var(--muted);margin:16px 0 24px}
.badge{position:absolute;top:30px;width:44px;height:44px;border-radius:50%;background:var(--green);border:3px solid var(--white);color:var(--white);font-size:12px;font-weight:700;display:flex;align-items:center;justify-content:center}
.post.left .badge{right:-22px}
.post.right .badge{left:-22px;z-index:2}
.photo.kale{background:radial-gradient(circle at 50% 55%,#4f7a2e 0 35%,transparent 36%),linear-gradient(160deg,#3d5e24,#7a9c4c 60%,#d8c7a6)}
.photo.oat{background:radial-gradient(circle at 50% 45%,#d9b27a 0 38%,transparent 39%),linear-gradient(160deg,#efe4d4,#c9a577)}
.photo.soup{background:radial-gradient(circle at 50% 50%,#f1d79b 0 30%,#fff5e6 31% 40%,transparent 41%),linear-gradient(160deg,#f6eee0,#d9c3a3)}
.photo.donut{background:radial-gradient(circle at 40% 35%,#5a3a2e 0 22%,transparent 23%),radial-gradient(circle at 62% 70%,#f3b8c6 0 22%,transparent 23%),linear-gradient(160deg,#7a4e3c,#c48a78)}
.pager{display:grid;grid-template-columns:280px 280px;height:50px}
.pager a{display:flex;align-items:center;justify-content:center;gap:8px;font-size:11px;font-weight:700;letter-spacing:.5px;text-decoration:none}
.pager .prev{background:var(--green-soft);color:var(--green)}
.pager .next{background:var(--green);color:var(--white)}

/* sidebar */
.sidebar{position:absolute;top:950px;left:760px;width:280px;height:1650px;background:var(--peach);padding:40px 26px}
.sidebar h4{font-size:18px;font-weight:700;text-align:center;color:var(--ink);margin-bottom:18px}
.avatar{width:150px;height:150px;border-radius:50%;margin:0 auto;border:5px solid var(--white);background:radial-gradient(circle at 50% 40%,#e8b7a0,#b97d6a 60%,#7c9a5e)}
.about p{font-size:11px;line-height:1.7;color:var(--muted);margin:18px 0;text-align:left}
.about .btn{margin:0 auto;display:flex;width:130px;justify-content:center}
.block{margin-top:60px}
.item{display:flex;gap:14px;align-items:center;margin-bottom:20px}
.thumb{width:54px;height:54px;border-radius:50%;flex:none}
.item b{display:block;font-size:12px;font-weight:700;color:var(--ink);line-height:1.3}
.item small{display:block;font-size:9px;color:var(--pink);font-weight:700;margin-top:4px}
.ad{margin-top:50px;height:300px;background:radial-gradient(ellipse at 50% 65%,#e9c989 0 35%,transparent 36%),linear-gradient(180deg,#f7efe2,#dfeccf)}

/* footer */
.footer{position:absolute;top:2660px;left:0;width:1200px;height:304px;background:linear-gradient(180deg,#f9c3cf,#fbd9d2 60%,#fde8dc);text-align:center}
.footer .up{position:absolute;left:584px;top:-16px;width:32px;height:32px;border-radius:50%;background:var(--coral)}
.footer .name{margin-top:60px;font-family:"Montserrat",sans-serif;font-weight:700;font-size:30px;color:var(--pink)}
.footer nav{margin-top:30px;display:flex;justify-content:center;gap:30px}
.footer nav a{font-size:11px;font-weight:700;color:var(--ink);text-decoration:none;letter-spacing:.5px}
.footer nav a.active{color:var(--pink)}
.footer .social{display:flex;justify-content:center;gap:12px;margin-top:22px}
.footer .social span{width:12px;height:12px;border-radius:50%;background:var(--pink)}
.footer .copy{font-size:10px;color:var(--muted);margin-top:22px}
</style>
</head>
<body>

<header class="topbar">
  <nav class="links"><a href="#">HOME</a><a href="#">ABOUT</a><a href="#" class="active">RECIPES</a><a href="#">RESOURCES</a></nav>
  <div class="social"><span></span><span></span><span></span><span></span><span></span></div>
</header>

<div class="brand"><span class="dot"></span><span class="name">TheHoneyedDays</span></div>

<nav class="wrap catnav">
  <a href="#">DESSERTS</a><a href="#">DONUTS</a><a href="#">CAKES</a><a href="#">CHOCOLATES</a><a href="#">SWEETS</a>
</nav>

<section class="wrap hero" role="img" aria-label="Warm photo of chocolate-frosted cupcakes on a table">
  <h1>“Gluten-free &amp; dairy-free sweets that actually taste good”</h1>
</section>

<section class="wrap newsletter">
  <h2>Subscribe Our Newsletter</h2>
  <p>Enter your email address to subscribe to this blog and receive notifications of new recipes by email.</p>
  <form><div class="field">Enter your email address</div><span class="btn">SIGN UP</span></form>
  <div class="donuts" role="img" aria-label="Colourful glazed donuts with sprinkles"></div>
</section>

<main class="posts">
  <article class="post left">
    <div class="photo kale" role="img" aria-label="Bowl of sautéed kale with lemon slices"><span class="badge">12</span></div>
    <div class="text">
      <h3>Sauteed Kale with Lemon and Ginger</h3>
      <div class="meta">March 20, 2014 &nbsp;·&nbsp; 12 Comments</div>
      <div class="cat">DINNER, LUNCH, VEGAN</div>
      <p>Kale never tasted this bright. A quick toss in the pan with fresh lemon and ginger makes a simple side you will want every night of the week.</p>
      <span class="btn">LEARN MORE</span>
    </div>
  </article>
  <article class="post right">
    <div class="text">
      <h3>Blueberry Chocolate Chip Oatmeal Minis</h3>
      <div class="meta">March 20, 2014 &nbsp;·&nbsp; 8 Comments</div>
      <div class="cat">DESSERT</div>
      <p>Little oat bites full of juicy berries and melty chips. They bake in minutes, keep well for days and make the perfect lunchbox treat for kids.</p>
      <span class="btn">READ MORE</span>
    </div>
    <div class="photo oat" role="img" aria-label="Blueberry chocolate chip oatmeal cookies"><span class="badge">8</span></div>
  </article>
  <article class="post left">
    <div class="photo soup" role="img" aria-label="Bowl of creamy potato soup topped with herbs"><span class="badge">5</span></div>
    <div class="text">
      <h3>Dairy-Free Creamy Potato Soup</h3>
      <div class="meta">March 20, 2014 &nbsp;·&nbsp; 5 Comments</div>
      <div class="cat">DINNER, SOUP</div>
      <p>Rich, velvety and totally dairy free. This cozy soup gets its creamy texture from blended potatoes and a splash of coconut milk.</p>
      <span class="btn">LEARN MORE</span>
    </div>
  </article>
  <article class="post right">
    <div class="text">
      <h3>Blueberry Chocolate Chip Oatmeal Minis</h3>
      <div class="meta">March 20, 2014 &nbsp;·&nbsp; 3 Comments</div>
      <div class="cat">DESSERT</div>
      <p>A sweet little batch for busy mornings. Soft in the middle, golden at the edges and ready before the coffee is done brewing.</p>
      <span class="btn">READ MORE</span>
    </div>
    <div class="photo donut" role="img" aria-label="Stack of chocolate and pink glazed donuts"><span class="badge">3</span></div>
  </article>
  <nav class="pager"><a href="#" class="prev">◂ PREV POSTS</a><a href="#" class="next">NEXT POSTS ▸</a></nav>
</main>

<aside class="sidebar">
  <section class="about">
    <h4>Meet Me</h4>
    <div class="avatar" role="img" aria-label="Portrait photo of Rosalind"></div>
    <p>Welcome to TheHoneyedDays! I'm Rosalind, a mom who bakes sweets without gluten or dairy that still taste wonderful. Grab a cup and stay a while.</p>
    <span class="btn">READ MORE</span>
  </section>
  <section class="block">
    <h4>Recent Posts</h4>
    <div class="item"><span class="thumb" style="background:linear-gradient(135deg,#f5d6a0,#e7a77c)" role="img" aria-label="Swirl popcorn"></span><div><b>Christmas Swirl Popcorn</b><small>12 COMMENTS</small></div></div>
    <div class="item"><span class="thumb" style="background:linear-gradient(135deg,#cfe0a8,#8fb060)" role="img" aria-label="Broccoli soup"></span><div><b>Cream of Broccoli Soup (Dairy-free)</b><small>8 COMMENTS</small></div></div>
  </section>
  <section class="block">
    <h4>Most Popular</h4>
    <div class="item"><span class="thumb" style="background:linear-gradient(135deg,#f7d98a,#e9a94c)" role="img" aria-label="Mac and cheese"></span><div><b>Gluten Free Mac n Cheese</b><small>24 COMMENTS</small></div></div>
    <div class="item"><span class="thumb" style="background:linear-gradient(135deg,#8a5a48,#e6b3b8)" role="img" aria-label="Chocolate bark"></span><div><b>Peanut Peppermint Chocolate Bark</b><small>18 COMMENTS</small></div></div>
    <div class="item"><span class="thumb" style="background:linear-gradient(135deg,#f6ead2,#dcc08e)" role="img" aria-label="Potato soup"></span><div><b>Dairy Free Creamy Potato Soup</b><small>15 COMMENTS</small></div></div>
  </section>
  <div class="ad" role="img" aria-label="Promotion for a vegan chickpea salad sandwich recipe"></div>
</aside>

<footer class="footer">
  <span class="up"></span>
  <div class="name">TheHoneyedDays</div>
  <nav><a href="#" class="active">HOME</a><a href="#">ABOUT</a><a href="#">RECIPES</a><a href="#">RESOURCES</a></nav>
  <div class="social"><span></span><span></span><span></span><span></span><span></span></div>
  <p class="copy">Copyright © 2014 TheHoneyedDays.com. All rights reserved.</p>
</footer>

</body>
</html>
```